Bramblewood Coatings of Central Florida, LLC. Start-up painting business needs a professional web desig

We have a start up painting business that would like to reach/focus on commercial clients like building contractors, HOA's, apartment complexes, etc.. We would like a residential aspect to the web design as well. We have an existing website at "trybramblewoodcoats.com" with usable content. Have logo and color scheme attached. Use provided website ONLY as template. Add commercial services page. Can type own content when needed.

Industry/Entity Type

Apartment

Number of Pages Required

5+ page

Font styles to use
Serif
Sans Serif
Decorative
Script

Requirements
Must have
• Commercial services

```html
<!DOCTYPE html>
<html lang="en">
<head>
<meta charset="utf-8">
<title>Bramblewood Coatings of Central Florida, LLC</title>
<link href="https://fonts.googleapis.com/css2?family=Montserrat:ital,wght@0,400;0,600;0,700;1,400&family=Open+Sans:wght@400;600;700&display=swap" rel="stylesheet">
<style>
:root{
  --page:#ebebeb;
  --olive:#4d4c39;
  --olive-dark:#3a3a2b;
  --salmon:#d98571;
  --ink:#2b2b2b;
  --text:#555;
  --muted:#8a8a8a;
  --white:#fff;
  --contact:#262626;
  --line:#d6d6d6;
}
*{box-sizing:border-box;margin:0;padding:0}
html,body{width:1200px;height:5158px;overflow:hidden}
body{background:var(--page);font-family:"Open Sans",Arial,sans-serif;color:var(--text);position:relative}
.section{position:absolute}
h2.title{font-family:"Montserrat",Arial,sans-serif;font-weight:700;color:var(--ink);text-align:center;font-size:30px;letter-spacing:.5px}
.p{font-size:12px;line-height:1.7}

.topbar{top:0;left:0;width:1200px;height:28px;background:var(--olive-dark);color:#ddd;font-size:11px;display:flex;justify-content:space-between;align-items:center;padding:0 200px;font-family:"Montserrat",sans-serif}
.topbar b{color:#fff;font-weight:600;margin-right:10px}

.hero{top:28px;left:0;width:1200px;height:472px;background:linear-gradient(180deg,#d6d3ce 0%,#b9b6b0 45%,#8e8b86 100%)}
.header{position:absolute;top:0;left:180px;width:840px;height:92px;display:flex;align-items:center;justify-content:space-between}
.brand{display:flex;align-items:center;gap:12px;font-family:"Montserrat",sans-serif;font-weight:700;font-size:15px;color:var(--olive-dark);line-height:1.15;width:260px}
.brand .mark{width:34px;height:34px;background:var(--salmon);flex:none}
.nav{display:flex;gap:30px;align-items:center;font-family:"Montserrat",sans-serif;font-size:12px;font-weight:600;color:var(--olive-dark)}
.hero-copy{position:absolute;top:220px;width:1200px;text-align:center;color:#fff;font-family:"Montserrat",sans-serif}
.hero-copy .welcome{font-style:italic;font-size:28px}
.hero-copy h1{font-size:46px;font-weight:700;letter-spacing:1px;margin-top:6px}
.btn{display:inline-block;background:var(--salmon);color:#fff;font-family:"Montserrat",sans-serif;font-weight:600;font-size:13px;padding:14px 34px;letter-spacing:.5px}
.hero-copy .btn{margin-top:24px}

.about{top:500px;left:190px;width:825px;height:325px;background:var(--white);padding:40px 36px;display:flex;gap:34px}
.about h2{font-family:"Montserrat",sans-serif;font-size:30px;color:var(--ink);margin-bottom:14px}
.about h3{font-size:14px;color:var(--ink);margin-bottom:10px;font-weight:600}
.about .p{margin-bottom:10px}
.about .photo{flex:none;width:300px;height:200px;background:linear-gradient(160deg,#efece8,#c9c3bb 60%,#8f7a68)}

.brush{position:absolute;background:var(--salmon);border-radius:6px;opacity:.9}

.showcase{top:887px;left:162px;width:876px;height:901px;background:var(--olive);color:#fff;text-align:center}
.showcase .kicker{font-family:"Montserrat",sans-serif;font-size:14px;margin-top:26px}
.showcase h2{font-family:"Montserrat",sans-serif;font-size:30px;font-weight:700}
.video{position:absolute;left:206px;top:120px;width:466px;height:248px;background:linear-gradient(180deg,#b9c4cc,#e8e6df 55%,#9a8f7b)}
.video .bar{height:26px;background:rgba(0,0,0,.55);font-size:11px;text-align:left;padding:6px 10px}
.video .play{position:absolute;left:213px;top:104px;width:40px;height:28px;background:rgba(20,20,20,.85);border-radius:6px}
.video .play:after{content:"";position:absolute;left:16px;top:8px;border-left:11px solid #fff;border-top:6px solid transparent;border-bottom:6px solid transparent}
.video .label{position:absolute;left:10px;bottom:8px;font-size:11px;text-align:left}
.showcase h2.port{position:absolute;top:452px;width:876px}
.cards{position:absolute;top:540px;left:27px;display:flex;gap:20px}
.card{width:193px;height:258px;background:#fff;color:var(--ink)}
.card .img{height:196px}
.card .cap{font-family:"Montserrat",sans-serif;font-size:12px;font-weight:600;padding-top:12px}
.card .sub{font-size:9px;color:var(--muted);margin-top:4px}
.dots{position:absolute;top:834px;width:876px;display:flex;justify-content:center;gap:6px}
.dots i{width:8px;height:8px;border-radius:50%;background:#fff;opacity:.6}
.dots i:first-child{opacity:1}

.services{top:1857px;left:162px;width:876px;height:1255px;background:#fff}
.services h2{margin-top:54px}
.services .intro{width:580px;margin:10px auto 0;text-align:center;font-size:12px;line-height:1.6}
.spine{position:absolute;left:437px;top:220px;width:2px;height:940px;background:var(--line)}
.node{position:absolute;left:368px;width:140px;height:140px;border-radius:50%;border:5px solid #fff;box-shadow:0 0 0 1px var(--line)}
.entry{position:absolute;width:310px;font-size:11px;line-height:1.6}
.entry.left{left:40px;text-align:right}
.entry.right{left:530px}
.entry .date{font-family:"Montserrat",sans-serif;font-weight:700;font-size:12px;color:var(--ink)}
.entry h4{font-family:"Montserrat",sans-serif;font-size:14px;color:var(--salmon);margin-bottom:6px}
.entry ul{list-style:none;margin:4px 0}
.entry li:before{content:"• "}
.story{position:absolute;left:388px;top:1112px;width:100px;height:100px;border-radius:50%;background:var(--olive);color:#fff;font-family:"Montserrat",sans-serif;font-weight:700;font-size:12px;text-align:center;display:flex;align-items:center;justify-content:center;line-height:1.3}

.team{top:3181px;left:162px;width:876px;height:526px;background:linear-gradient(180deg,#f1efeb,#e4e1dc)}
.team h2{margin-top:40px}
.members{position:absolute;top:150px;left:0;width:876px;display:flex;justify-content:center;gap:50px}
.member{width:160px;text-align:center}
.member .face{width:160px;height:160px;border-radius:50%;border:6px solid #fff;background:linear-gradient(160deg,#e3d6c8,#c6a993)}
.member .name{font-family:"Montserrat",sans-serif;font-size:13px;font-weight:600;color:var(--ink);margin-top:12px}
.member .role{font-size:10px;color:var(--muted)}
.member .social{display:flex;justify-content:center;gap:8px;margin-top:8px}
.member .social i{width:20px;height:20px;border-radius:50%;background:#3f8fc7}
.team .p{position:absolute;top:398px;left:238px;width:400px;text-align:center;font-size:11px}

.creds{top:3772px;left:162px;width:876px;height:251px;background:#fff}
.creds h2{margin-top:54px;font-size:26px}
.badges{display:flex;justify-content:center;align-items:center;gap:60px;margin-top:36px}
.badges span{background:#9aa3a6}

.map{top:4092px;left:162px;width:876px;height:406px;background:linear-gradient(135deg,#e7e4dc,#d9d8cf 50%,#e4e0d6)}

.contact{top:4567px;left:162px;width:876px;height:488px;background:var(--contact);color:#ccc}
.contact h2{color:#fff;margin-top:44px}
.info{position:absolute;left:90px;top:118px;font-size:11px;line-height:1.8;display:flex;gap:40px}
.info .mark{width:30px;height:30px;background:var(--salmon);margin-bottom:6px}
.field{position:absolute;background:#fff;height:34px;width:250px;color:#999;font-size:10px;padding:10px 12px}
.field.area{height:150px;width:300px}
.contact .btn{position:absolute;left:360px;top:396px;padding:12px 58px;font-size:12px}

.footer{top:5072px;left:0;width:1200px;height:86px;background:#fff;display:flex;align-items:center;padding:0 190px;font-size:10px;color:var(--muted)}
.footer .social{position:absolute;left:540px;display:flex;gap:8px}
.footer .social i{width:24px;height:24px;border-radius:50%;background:var(--salmon)}
</style>
</head>
<body>

<div class="section topbar"><span>1180 HERON MARSH LANE | LAKELAND, FL 33811</span><span><b>CONTACT US TODAY</b>(+1 863) 555-0148</span></div>

<div class="section hero" role="img" aria-label="Bright living room interior with white sofa and shelving">
  <div class="header">
    <div class="brand"><span class="mark"></span><span>Bramblewood Coatings<br>of Central Florida, LLC</span></div>
    <nav class="nav"><span>HOME</span><span>ABOUT</span><span>SERVICES</span><span>CONTACT US</span>
      <svg width="14" height="14" viewBox="0 0 14 14"><circle cx="6" cy="6" r="4.5" fill="none" stroke="#3a3a2b" stroke-width="2"/><line x1="9.5" y1="9.5" x2="13" y2="13" stroke="#3a3a2b" stroke-width="2"/></svg></nav>
  </div>
  <div class="hero-copy">
    <div class="welcome">Welcome To Bramblewood Coatings of Central Florida, LLC.</div>
    <h1>WHERE DREAMS MEET REALITY</h1>
    <span class="btn">EXPLORE COLOR CENTER</span>
  </div>
</div>

<div class="section about">
  <div>
    <h2>ABOUT</h2>
    <h3>Home painting done right.</h3>
    <p class="p">At Bramblewood Coatings of Central Florida, we paint homes, HOA communities, apartment complexes and job sites for building contractors with the same care.</p>
    <p class="p">Bring a high-quality finish to your home or property with a crew that works clean, on schedule and with respect from start to finish.</p>
    <p class="p">Call us today for a free estimate. Get your painting project started!</p>
  </div>
  <div class="photo" role="img" aria-label="Modern bathroom with wooden vanity"></div>
</div>

<div class="brush" style="left:400px;top:842px;width:150px;height:30px;transform:rotate(-24deg)"></div>
<div class="brush" style="left:150px;top:1800px;width:180px;height:26px;transform:rotate(-18deg);background:var(--olive)"></div>
<div class="brush" style="left:520px;top:1812px;width:160px;height:30px;transform:rotate(-20deg)"></div>
<div class="brush" style="left:480px;top:3125px;width:200px;height:30px;transform:rotate(-16deg)"></div>
<div class="brush" style="left:490px;top:4030px;width:150px;height:26px;transform:rotate(-20deg);background:#e0cdbf"></div>
<div class="brush" style="left:470px;top:4470px;width:220px;height:40px;transform:rotate(-22deg)"></div>

<div class="section showcase">
  <div class="kicker">check out our</div>
  <h2>COMPANY VIDEO</h2>
  <div class="video" role="img" aria-label="Company video still of a white columned house">
    <div class="bar">Bramblewood Coatings Intro</div>
    <div class="play"></div>
    <div class="label">Bramblewood Coatings of Central Florida, LLC.</div>
  </div>
  <h2 class="port">OUR PROTFOLIO</h2>
  <div class="cards">
    <div class="card"><div class="img" role="img" aria-label="White bathroom" style="background:linear-gradient(160deg,#ecebe8,#b7b3ad)"></div><div class="cap">Bathroom</div><div class="sub">Clean refresh, modern finish</div></div>
    <div class="card"><div class="img" role="img" aria-label="Modern interior living room" style="background:linear-gradient(160deg,#d8d8d8,#6f6f6f)"></div><div class="cap">Modern Interior Design</div><div class="sub">Bold contrast, crisp lines</div></div>
    <div class="card"><div class="img" role="img" aria-label="Painter rolling yellow wall" style="background:linear-gradient(160deg,#f0d25a,#c89a3a)"></div><div class="cap">Painting Services</div><div class="sub">Rolled, brushed and sprayed</div></div>
    <div class="card"><div class="img" role="img" aria-label="Colour swatch fan" style="background:linear-gradient(135deg,#e8c04a,#d9715c 50%,#6d9cc6)"></div><div class="cap">Trademark House Painting</div><div class="sub">Colors chosen with care</div></div>
  </div>
  <div class="dots"><i></i><i></i><i></i></div>
</div>

<div class="section services">
  <h2 class="title">SERVICES</h2>
  <p class="intro">We offer residential and commercial services for homeowners, building contractors, HOAs and apartment complexes. When a project comes up, planned or not, we take the guess work out of the way with our worry free guarantee.</p>
  <div class="spine"></div>

  <div class="node" style="top:223px;background:linear-gradient(160deg,#9cc3e0,#8a6a4c)" role="img" aria-label="Worker on a ladder"></div>
  <div class="entry left" style="top:220px"><div class="date">JULY 2010</div><h4>Repair Services</h4>
    <p>No matter what the project, there will be repairs needed to a wall or trim board. We handle minor repair work before painting so the finish lasts.</p>
    <p><b>Repairs included in all services:</b></p>
    <ul><li>Drywall repair - less than 1 inch of damage</li><li>Caulking</li><li>Quotes to cover all materials needed</li></ul></div>

  <div class="node" style="top:446px;background:linear-gradient(160deg,#f2e3b8,#b58a4a)" role="img" aria-label="Interior room with warm lighting"></div>
  <div class="entry right" style="top:470px"><div class="date">JANUARY 2011</div><h4>Interior Design Services</h4>
    <p>Picking the right color is the hardest part of the job. Browse our collections with confidence and we help you choose tones that match your space.</p>
    <p>Call us first so we can guide your project from beginning to end with our team of paint specialists.</p></div>

  <div class="node" style="top:687px;background:linear-gradient(160deg,#e6c45a,#a9452f)" role="img" aria-label="Paint cans and brushes from above"></div>
  <div class="entry left" style="top:680px"><div class="date">DECEMBER 2012</div><h4>Interior Painting Services</h4>
    <p>Sometimes a coat of paint is all a room needs for a fresh look. From single homes to apartment units between tenants, we cover both.</p>
    <p><b>Included in all interior invoices:</b></p>
    <ul><li>Custom colors</li><li>Wallpaper removal and hanging</li><li>Wall sealing</li><li>Trim finishing</li><li>Unit turnovers for apartment complexes</li></ul></div>

  <div class="node" style="top:910px;background:linear-gradient(160deg,#d9cfc0,#7a5a3e)" role="img" aria-label="Painter brushing exterior trim"></div>
  <div class="entry right" style="top:900px"><div class="date">FEBRUARY 2014</div><h4>Exterior &amp; Commercial Services</h4>
    <p>Exterior work takes hours, so leave it to the professionals. We paint homes and large commercial properties with safe, precise crews.</p>
    <ul><li>New builds for building contractors</li><li>HOA community repaints</li><li>Apartment complex exteriors</li><li>Pressure washing and repairs</li></ul>
    <p>Ask about scheduled maintenance plans for your property.</p></div>

  <div class="story">OUR<br>STORY<br>CONTINUES<br>...</div>
</div>

<div class="section team">
  <h2 class="title">OUR TEAM</h2>
  <div class="members">
    <div class="member"><div class="face" role="img" aria-label="Portrait of team member"></div><div class="name">Dana Whitfield</div><div class="role">Founder</div><div class="social"><i></i><i style="background:#3b5a9a"></i></div></div>
    <div class="member"><div class="face" role="img" aria-label="Portrait of team member" style="background:linear-gradient(160deg,#c9b8a8,#8e6f58)"></div><div class="name">Marcus Ellery</div><div class="role">CEO</div><div class="social"><i></i><i style="background:#3b5a9a"></i></div></div>
    <div class="member"><div class="face" role="img" aria-label="Portrait of team member" style="background:linear-gradient(160deg,#f0d3b0,#c9875a)"></div><div class="name">Nora Castell</div><div class="role">Interior Designer</div><div class="social"><i></i><i style="background:#3b5a9a"></i></div></div>
  </div>
  <p class="p">Our crew has painted homes and commercial properties across Central Florida for years, bringing care, skill and a tidy finish to every job.</p>
</div>

<div class="section creds">
  <h2 class="title">CHECK OUT OUR CREDENTIALS</h2>
  <div class="badges">
    <span style="width:60px;height:60px;border-radius:50%;background:#c9a640"></span>
    <span style="width:110px;height:40px"></span>
    <span style="width:110px;height:40px;background:#7f8fb0"></span>
    <span style="width:64px;height:64px;border-radius:50%"></span>
    <span style="width:70px;height:50px;border-radius:50%;background:#6fa67a"></span>
  </div>
</div>

<div class="section map" role="img" aria-label="Street map of Lakeland with location marker">
  <svg style="position:absolute;left:418px;top:130px" width="40" height="56" viewBox="0 0 40 56"><path d="M20 0C9 0 0 9 0 20c0 15 20 36 20 36s20-21 20-36C40 9 31 0 20 0z" fill="#e0463c"/><circle cx="20" cy="20" r="7" fill="#fff"/></svg>
</div>

<div class="section contact">
  <h2 class="title">CONTACT US</h2>
  <div class="info">
    <div><div class="mark"></div>1180 Heron Marsh Lane<br>Lakeland, FL<br>33811</div>
    <div>(+1 863) 555-0148<br>hello@trybramblewoodcoats.com</div>
    <div style="margin-left:110px">(+1 863) 555-0162<br>team@trybramblewoodcoats.com</div>
  </div>
  <div class="field" style="left:90px;top:240px">YOUR NAME *</div>
  <div class="field" style="left:90px;top:288px">YOUR EMAIL *</div>
  <div class="field" style="left:90px;top:336px">SUBJECT</div>
  <div class="field area" style="left:470px;top:220px">YOUR MESSAGE *</div>
  <span class="btn">SUBMIT</span>
</div>

<div class="section footer">
  <span>© Copyright 2016 Bramblewood Coatings of Central Florida, LLC</span>
  <div class="social"><i style="background:#3f8fc7"></i><i style="background:#3b5a9a"></i><i style="background:#d0463a"></i><i></i></div>
</div>

</body>
</html>
```